Logo and Business Card Design

Harbor Crest Logistics provides our customers with one call solutions to packing, trucking and warehousing needs throughout the supply chain.
We need ideas for a logo/business card. I have 2 general concepts.
1. Modern logo involving: the globe, Harbor Crest, arrow, movement, the two words having 2 different fonts/colors, the number 1.
2. Logo involving Lion/Winged Lion: incorporate lion onto globe, tagline "The Pride of the Pack", movement, flowing.

Target Market(s)

International Logistics companies, Air cargo companies, manufacturing companies

Industry/Entity Type

Business

Contact Information for Business Card

Dale Verhoeven
Owner
Harbor Crest Logistics
2874 Wexley Blvd.
Elk Grove Village, IL 60219
555-308-2946
daleh@harborcrestfreight.example

Font styles to use
Sans Serif

Requirements
Must have
• 1. Modern logo involving: the globe, Harbor Crest, arrow, movement, the two words having 2 different fonts/colors, the number 1.
Nice to have
Should not have
• Do not have too complex of a design.

```html
<!DOCTYPE html>
<html lang="en">
<head>
<meta charset="utf-8">
<title>Harbor Crest Logistics – Business Card</title>
<link rel="stylesheet" href="https://fonts.googleapis.com/css2?family=Exo+2:wght@400;600&display=swap">
<style>
  :root {
    --backdrop: #e6e8eb;
    --card: #ffffff;
    --ink: #3a3f47;
    --brand-blue: #1f4fc4;
    --deep-blue: #163a9c;
    --sky-blue: #3f8fe6;
    --pale-blue: #cfe2f7;
    --on-blue: #ffffff;
  }
  * { margin: 0; padding: 0; box-sizing: border-box; }
  html, body { width: 1200px; height: 900px; overflow: hidden; }
  body {
    background: var(--backdrop);
    font-family: "Exo 2", sans-serif;
    color: var(--ink);
    display: flex;
    flex-direction: column;
    align-items: center;
    justify-content: center;
    gap: 36px;
  }
  .card {
    position: relative;
    width: 700px;
    height: 400px;
    background: var(--card);
    border-radius: 40px;
    overflow: hidden;
    box-shadow: 0 6px 18px rgba(0,0,0,0.12);
  }
  .card-art { position: absolute; inset: 0; width: 100%; height: 100%; }
  .contact {
    position: absolute;
    left: 40px;
    top: 36px;
    list-style: none;
    font-size: 15px;
    line-height: 1.35;
  }
  .contact .address { margin-bottom: 12px; }
  .contact .line { display: flex; align-items: center; gap: 8px; margin-bottom: 5px; font-size: 13px; }
  .contact svg { width: 13px; height: 13px; flex: none; }
  .brand {
    position: absolute;
    display: flex;
    align-items: center;
    gap: 12px;
    color: var(--brand-blue);
    font-weight: 600;
    letter-spacing: 1px;
  }
  .brand-dot { border-radius: 50%; background: var(--brand-blue); flex: none; }
  .card-front .brand { left: 340px; top: 150px; font-size: 40px; }
  .card-front .brand-dot { width: 30px; height: 30px; }
  .card-back .brand { left: 50%; top: 50%; transform: translate(-50%, -50%); font-size: 54px; }
  .card-back .brand-dot { width: 40px; height: 40px; }
  .holder {
    position: absolute;
    right: 50px;
    bottom: 34px;
    text-align: right;
    color: var(--on-blue);
  }
  .holder-name { font-size: 19px; font-weight: 600; letter-spacing: 1px; text-transform: uppercase; }
  .holder-role { font-size: 15px; }
</style>
</head>
<body>

<section class="card card-front">
  <svg class="card-art" viewBox="0 0 700 400" preserveAspectRatio="none" aria-hidden="true">
    <path d="M0 215 C180 300 420 320 700 282 L700 400 L0 400 Z" fill="var(--pale-blue)"/>
    <path d="M0 232 C190 318 430 336 700 298 L700 400 L0 400 Z" fill="var(--sky-blue)"/>
    <path d="M0 262 C200 342 450 352 700 318 L700 400 L0 400 Z" fill="var(--brand-blue)"/>
    <path d="M0 300 C220 370 470 372 700 340 L700 400 L0 400 Z" fill="var(--deep-blue)"/>
    <path d="M20 250 C220 332 460 344 690 306" fill="none" stroke="var(--on-blue)" stroke-width="3" opacity="0.85"/>
  </svg>

  <ul class="contact">
    <li class="address">2874 Wexley Blvd.<br>Elk Grove Village, IL 60219</li>
    <li class="line">
      <svg viewBox="0 0 16 16"><rect x="4" y="1" width="8" height="14" rx="1.5" fill="none" stroke="currentColor" stroke-width="1.5"/></svg>
      555-308-2946
    </li>
    <li class="line">
      <svg viewBox="0 0 16 16"><path d="M3 2h3l1 4-2 1a8 8 0 0 0 4 4l1-2 4 1v3a1 1 0 0 1-1 1A12 12 0 0 1 2 3a1 1 0 0 1 1-1z" fill="currentColor"/></svg>
      555-308-2946
    </li>
    <li class="line">
      <svg viewBox="0 0 16 16"><rect x="1" y="3" width="14" height="10" rx="1" fill="none" stroke="currentColor" stroke-width="1.5"/><path d="M1 4l7 5 7-5" fill="none" stroke="currentColor" stroke-width="1.5"/></svg>
      daleh@harborcrestfreight.example
    </li>
    <li class="line">
      <svg viewBox="0 0 16 16"><circle cx="8" cy="8" r="6.5" fill="none" stroke="currentColor" stroke-width="1.5"/><path d="M1.5 8h13M8 1.5c-3 3-3 10 0 13M8 1.5c3 3 3 10 0 13" fill="none" stroke="currentColor" stroke-width="1.2"/></svg>
      www.harborcrestfreight.example
    </li>
  </ul>

  <div class="brand"><span class="brand-dot"></span><span class="brand-name">Harbor Crest</span></div>

  <div class="holder">
    <p class="holder-name">Dale Verhoeven</p>
    <p class="holder-role">Owner</p>
  </div>
</section>

<section class="card card-back">
  <div class="brand"><span class="brand-dot"></span><span class="brand-name">Harbor Crest</span></div>
</section>

</body>
</html>
```